Ad design for a macarons brand

We are a dessert brand with one product line: macarons. Our products delight. Every bite is a dream!

We are launching a new product and would like to lunch a small tactical campaign for the product to boost sales.

The new macron is mango ganache and the middle a mix of sour mango and yuzu (https://www.plumvarell.com/about-the-fruit-584302).

Here are some images we took of the new macaron
https://www.fennlocker.com/sh/qrtwpzhkvbmls/AAFJtRWD-nxPlkhQZ7CeW4DLp?dl=0

I attach the brand guideline document.

Required sizes

1080 x 1350
1080 x 1920

```html
<!DOCTYPE html>
<html lang="en">
<head>
<meta charset="utf-8">
<title>Mango Ganache – Launch Ad</title>
<link rel="stylesheet" href="https://fonts.googleapis.com/css2?family=DM+Serif+Display&family=Fredoka:wght@600&family=Hind:wght@700&display=swap">
<style>
  :root {
    --bg-light: #fbdf5a;
    --bg-deep: #ffc10f;
    --headline: #c96f08;
    --headline-shadow: rgba(214, 140, 20, 0.45);
    --title: #f9bd0c;
    --title-edge: #c98406;
    --title-glow: rgba(120, 70, 0, 0.35);
    --subtitle: #8b5a0e;
    --band: #fcdc0a;
    --tagline: #c8840a;
    --logo: #ffffff;
    --splash-light: #ffd84a;
    --splash-deep: #f6b21a;
    --cookie-light: #f6c46a;
    --cookie-deep: #e9892a;
    --shadow: rgba(150, 110, 10, 0.45);
  }
  * { margin: 0; padding: 0; box-sizing: border-box; }
  html, body { width: 675px; height: 1200px; overflow: hidden; }
  .ad {
    position: relative;
    width: 675px;
    height: 1200px;
    overflow: hidden;
    background: linear-gradient(160deg, var(--bg-light) 0%, var(--bg-light) 30%, var(--bg-deep) 100%);
  }
  .ad__kicker {
    position: absolute;
    top: 56px;
    left: 0;
    width: 100%;
    padding-left: 34px;
    text-align: center;
    font-family: "Hind", sans-serif;
    font-weight: 700;
    font-size: 46px;
    line-height: 1;
    color: var(--headline);
    text-shadow: 3px 3px 0 var(--headline-shadow);
  }
  .ad__splash {
    position: absolute;
    top: 150px;
    left: 98px;
    width: 490px;
    height: 425px;
    border-radius: 46% 54% 42% 58% / 48% 40% 60% 52%;
    background: radial-gradient(ellipse at 60% 40%, var(--splash-deep) 0%, var(--splash-light) 70%, rgba(255, 216, 74, 0) 100%);
  }
  .ad__title {
    position: absolute;
    top: 236px;
    left: 0;
    width: 100%;
    text-align: center;
    font-family: "Fredoka", sans-serif;
    font-weight: 600;
    line-height: 1;
    color: var(--title);
    -webkit-text-stroke: 2px var(--title-edge);
    text-shadow: 3px 4px 6px var(--title-glow);
  }
  .ad__title-line { display: block; }
  .ad__title-line--first { font-size: 108px; padding-left: 28px; }
  .ad__title-line--second { font-size: 116px; margin-top: 6px; }
  .ad__subtitle {
    position: absolute;
    top: 500px;
    left: 0;
    width: 100%;
    padding-left: 8px;
    text-align: center;
    font-family: "DM Serif Display", serif;
    font-size: 18px;
    letter-spacing: 0.4px;
    color: var(--subtitle);
  }
  .ad__product {
    position: absolute;
    top: 694px;
    left: 247px;
    width: 173px;
    height: 187px;
    border-radius: 40% / 28%;
    background: linear-gradient(180deg, var(--cookie-deep) 0%, var(--cookie-light) 45%, var(--cookie-light) 100%);
  }
  .ad__product-shadow {
    position: absolute;
    top: 903px;
    left: 0;
  }
  .ad__band {
    position: absolute;
    left: 0;
    bottom: 0;
    width: 100%;
    height: 88px;
    background: var(--band);
  }
  .ad__badge {
    position: absolute;
    left: 251px;
    top: 1026px;
    width: 172px;
    height: 172px;
    border-radius: 50%;
    background: var(--band);
  }
  .ad__brand {
    position: absolute;
    top: 1090px;
    left: 0;
    width: 100%;
    text-align: center;
    font-family: "DM Serif Display", serif;
    font-size: 28px;
    line-height: 1;
    color: var(--logo);
  }
  .ad__tagline {
    position: absolute;
    top: 1146px;
    left: 0;
    width: 100%;
    text-align: center;
    font-family: "DM Serif Display", serif;
    font-size: 31px;
    line-height: 1;
    letter-spacing: 0.5px;
    color: var(--tagline);
  }
</style>
</head>
<body>
  <main class="ad">
    <h2 class="ad__kicker">INTRODUCING</h2>

    <div class="ad__splash" role="img" aria-label="Mango juice splash with droplets behind the product name"></div>
    <h1 class="ad__title">
      <span class="ad__title-line ad__title-line--first">Mango</span>
      <span class="ad__title-line ad__title-line--second">Ganache</span>
    </h1>
    <p class="ad__subtitle">A mix of sour mango &amp; yuzu</p>

    <div class="ad__product" role="img" aria-label="Photo of the mango ganache macaron split into top shell, mango-yuzu filling and bottom shell"></div>
    <svg class="ad__product-shadow" width="675" height="26" viewBox="0 0 675 26" aria-hidden="true">
      <defs>
        <radialGradient id="floor-shadow">
          <stop offset="0%" stop-color="rgba(150,110,10,0.45)"/>
          <stop offset="100%" stop-color="rgba(150,110,10,0)"/>
        </radialGradient>
      </defs>
      <ellipse cx="337" cy="13" rx="105" ry="12" fill="url(#floor-shadow)"/>
    </svg>

    <div class="ad__band"></div>
    <div class="ad__badge"></div>
    <p class="ad__brand">Maylune</p>
    <p class="ad__tagline">Every bite's a dream!</p>
  </main>
</body>
</html>
```